Glow in the Dark Inks Sales Flyer - Targeted to the music industry

We need help!
We need a creative flyer to tell the music industry about our new, colorful glow in the dark inks that look amazing on T-shirts and concert merchandise.

The flyer will go to merchandising managers for bands around the world. The design needs to be hip and contemporary but not offensive. No f-bombs please! Size is 4” x 6” or 3” x 5”, and will be printed on card stock. Design can be both sides if you want. We expect color but black and white with some fluorescent accents could be cool. Surprise us.
Here’s some copy, and we can fill in the contact info when the design is close to final.

Help your fans get lit with branded T-shirts and merchandise that glows in the dark!

Let our new Starwell Inks light up your next show!

Call us now –
Updates

Hello Designers.

Please keep in mind that although the thought of glow-in-the-dark may trigger a glowing, green color in your creative minds, StarWell Inks has a wide variety of colors to bring to offer. So please be sure to show that it's not only green glow we are promoting but we have a wide range of colors that glow (including pink, purple, white that glow blue, blue, green, orange, yellow, etc.)

Thank you!

```html
<!DOCTYPE html>
<html lang="en">
<head>
<meta charset="utf-8">
<title>Starwell Inks – Glow in the Dark Flyer</title>
<link href="https://fonts.googleapis.com/css2?family=Special+Elite&display=swap" rel="stylesheet">
<style>
  :root {
    --page: #ffffff;
    --card: #050505;
    --ink: #f4f4ef;
    --glow-green: #3fd14a;
    --glow-yellow: #e8d21c;
    --glow-orange: #ff7a1a;
    --glow-red: #e8243a;
    --glow-pink: #e83fae;
    --glow-purple: #7a3fd8;
    --glow-blue: #2f6fe0;
  }
  html, body {
    margin: 0;
    padding: 0;
    width: 1200px;
    height: 1070px;
    overflow: hidden;
    background: var(--page);
  }
  .flyer {
    position: absolute;
    left: 70px;
    top: 339px;
    width: 1125px;
    height: 731px;
    background: var(--card);
    overflow: hidden;
    font-family: "Special Elite", "Courier New", monospace;
    color: var(--ink);
  }
  .glow-art {
    position: absolute;
    left: 40px;
    top: 140px;
    width: 1040px;
    height: 380px;
    background: linear-gradient(90deg,
      var(--glow-green) 0%, var(--glow-green) 14%,
      var(--glow-yellow) 30%, var(--glow-orange) 44%,
      var(--glow-red) 54%, var(--glow-pink) 64%,
      var(--glow-purple) 78%, var(--glow-blue) 100%);
    filter: blur(30px);
    opacity: 0.8;
    -webkit-mask-image: linear-gradient(180deg, transparent 0%, #000 25%, #000 70%, transparent 100%);
    mask-image: linear-gradient(180deg, transparent 0%, #000 25%, #000 70%, transparent 100%);
  }
  .call-out {
    position: absolute;
    left: 10px;
    top: 82px;
    width: 320px;
    text-align: center;
    font-size: 38px;
    line-height: 1.2;
    font-weight: bold;
    transform: rotate(-25deg);
    transform-origin: center;
  }
  .pitch {
    position: absolute;
    left: 345px;
    top: 62px;
    width: 710px;
    margin: 0;
    text-align: center;
    font-size: 44px;
    line-height: 58px;
    letter-spacing: 2px;
    font-weight: bold;
    white-space: nowrap;
  }
  .lead-in {
    position: absolute;
    left: 47px;
    top: 404px;
    margin: 0;
    font-size: 56px;
    line-height: 1;
    white-space: nowrap;
  }
  .brand-name {
    position: absolute;
    left: 147px;
    top: 478px;
    margin: 0;
    font-size: 170px;
    font-weight: normal;
    line-height: 1;
    white-space: nowrap;
    transform: scaleX(0.70);
    transform-origin: left top;
  }
  .sign-off {
    position: absolute;
    left: 47px;
    top: 624px;
    margin: 0;
    font-size: 61px;
    line-height: 1;
    white-space: nowrap;
  }
</style>
</head>
<body>
  <main class="flyer">
    <div class="glow-art" role="img" aria-label="Rainbow of glowing, dripping paint streaks in green, yellow, orange, red, pink, purple and blue"></div>

    <div class="call-out">CALL US NOW<br>555-014-2368</div>

    <p class="pitch">Help your fans get lit<br>with branded T-shirts and<br>merchandise that<br>glows in the dark!</p>

    <p class="lead-in">Let our new</p>
    <h1 class="brand-name">STARWELL INKS</h1>
    <p class="sign-off">light up your next show!</p>
  </main>
</body>
</html>
```